Beauty Salon Business/Appointment Card Design

We need a business card and logo design for our beauty business called Velora Beauty.

The name Velora is taken from the Sumerian goddesss of love, procreation, war and being honest with oneself. Her name was written with a sign that represents a reed stalk tied into a loop at the top, often depicted with wings as well wearing lapis lazuli jewels.

We will be offering all spa and beauty services and want to create a peaceful, revitalising environment for people to come and be welcomed, enabling them to find the beauty within themselves.

We would also prefer simplicity and boldness in a design, as well as an element of individuality and reproducibility for letterheads and other marketing products.

Project Deadline Extended
Reason: Due to work commitments, closing the due date at this time of the morning (0026 hrs) is not practical. We wll review the designs during the day of Wednesday the 11th and make a decision by 1700 hrs Australian Central Standard Time. Thank you all for your input and time

Target Market(s)

as its a beauty salon business, target is predominantly female from 18-60 years of age

Industry/Entity Type

Environment

Contact Information for Business Card

Velora Beauty (this is the business name - and needs a designed logo name/icon to be incorporated)

Dorrit - 0482 917 305

velorabeauty@mailquill.com.au

finding the beauty within (this is our business motto & can be in a different font from the rest)

Other font styles liked:
• always & forever; Beaked Tyrant

Requirements
Must have
• As these will also be doubling as appointment cards it is required that they be double sided in design with the reverse having the following information able to be written in:
day
date
time
Nice to have
• something that is different, catchy, instantly recognisable as this business

the front and back design should ideally be consistent and complimentary

```html
<!DOCTYPE html>
<html lang="en">
<head>
<meta charset="utf-8">
<title>Velora Beauty – Business &amp; Appointment Card</title>
<link rel="stylesheet" href="https://fonts.googleapis.com/css2?family=Courgette&family=Handlee&display=swap">
<style>
  :root {
    --backdrop: #e8e5e1;
    --card-dark: #0b0b0b;
    --card-dark-sheen: #1e1e1e;
    --card-light: #ffffff;
    --gold-light: #f5c76a;
    --gold-mid: #d9a442;
    --gold-deep: #b07a22;
    --white: #ffffff;
    --ink: #2a2a2a;
    --rose: #c65aa8;
    --silhouette-grey: #e9e9ea;
    --rule: #3a3a3a;
  }
  * { box-sizing: border-box; margin: 0; padding: 0; }
  html, body { width: 1200px; height: 1200px; overflow: hidden; }
  body {
    background: var(--backdrop);
    font-family: "Courgette", cursive;
    position: relative;
  }
  .card {
    position: absolute;
    left: 138px;
    width: 924px;
    height: 570px;
    overflow: hidden;
    box-shadow: 0 6px 18px rgba(0,0,0,0.18);
  }
  .card--front {
    top: 26px;
    background: linear-gradient(160deg, var(--card-dark-sheen) 0%, var(--card-dark) 55%, #050505 100%);
  }
  .card--back {
    top: 608px;
    background: var(--card-light);
  }

  /* Brand name block */
  .brand {
    position: absolute;
    display: flex;
    align-items: center;
    gap: 16px;
    font-family: "Courgette", cursive;
    line-height: 1;
    white-space: nowrap;
  }
  .brand__dot {
    width: 22px; height: 22px; border-radius: 50%;
    background: var(--rose);
    flex: none;
  }
  .card--front .brand { left: 58px; top: 140px; font-size: 68px; color: var(--white); }
  .card--back .brand { left: 222px; top: 150px; font-size: 80px; color: var(--ink); }

  /* Illustrations */
  .illustration { position: absolute; }
  .illustration--hair-gold {
    right: 0; top: 0; width: 470px; height: 570px;
    background: linear-gradient(200deg, var(--gold-light) 0%, var(--gold-mid) 50%, var(--gold-deep) 100%);
    clip-path: path("M250 0 L470 0 L470 570 L215 570 C200 520 150 480 90 440 C40 400 50 330 75 280 C100 220 100 150 150 95 C185 55 215 25 250 0 Z");
  }
  .illustration--hair-faint {
    left: 0; top: 0; width: 300px; height: 570px;
    background: linear-gradient(180deg, var(--silhouette-grey) 0%, #f1f1f2 100%);
    clip-path: path("M0 0 L230 0 C185 80 210 160 175 240 C145 310 180 380 150 450 C130 500 145 540 135 570 L0 570 Z");
  }

  /* Front contact details */
  .contact { position: absolute; left: 54px; top: 346px; color: var(--white); }
  .contact__name { font-size: 38px; line-height: 1.2; color: var(--gold-mid); margin-bottom: 6px; letter-spacing: 1px; }
  .contact__line { font-size: 22px; letter-spacing: 1.5px; line-height: 36px; white-space: nowrap; }

  .motto {
    position: absolute;
    font-family: "Handlee", cursive;
    letter-spacing: 2px;
    white-space: nowrap;
    line-height: 1.2;
  }
  .card--front .motto { left: 150px; top: 500px; font-size: 38px; color: var(--white); }
  .card--back .motto { left: 245px; top: 508px; font-size: 28px; color: var(--ink); }

  /* Appointment fields */
  .appointment {
    position: absolute; left: 136px; top: 318px; width: 660px;
    list-style: none;
  }
  .appointment__field {
    display: flex; align-items: flex-end; height: 54px;
  }
  .appointment__label {
    width: 120px; font-size: 25px; color: var(--ink); letter-spacing: 1px;
  }
  .appointment__rule {
    flex: 1; border-bottom: 1.5px solid var(--rule); margin-bottom: 8px;
  }
</style>
</head>
<body>
  <section class="card card--front" aria-label="Business card front">
    <div class="illustration illustration--hair-gold" role="img" aria-label="Gold illustration of a woman's profile with long flowing hair"></div>
    <div class="brand"><span class="brand__name">Velora Beauty</span><span class="brand__dot"></span></div>
    <div class="contact">
      <p class="contact__name">Dorrit</p>
      <p class="contact__line">Phone : 0482 917 305</p>
      <p class="contact__line">Email : velorabeauty@mailquill.com.au</p>
    </div>
    <p class="motto">finding the beauty within</p>
  </section>

  <section class="card card--back" aria-label="Appointment card back">
    <div class="illustration illustration--hair-faint" role="img" aria-label="Faint grey illustration of a woman's profile with long flowing hair"></div>
    <div class="brand"><span class="brand__name">Velora Beauty</span><span class="brand__dot"></span></div>
    <ul class="appointment">
      <li class="appointment__field"><span class="appointment__label">Name</span><span class="appointment__rule"></span></li>
      <li class="appointment__field"><span class="appointment__label">Time</span><span class="appointment__rule"></span></li>
      <li class="appointment__field"><span class="appointment__label">Date</span><span class="appointment__rule"></span></li>
    </ul>
    <p class="motto">finding the beauty within</p>
  </section>
</body>
</html>
```